Business Card Design

We need a business card for a well established Semi Trailer Hire company. I am looking for a new start as we are moving so would like to update our Business Cards and Letter heads.
We hire Semi Trailers to Transport companies.
The colour of our Trailers are Cherry Red so this must be the prominent colour.
I do not want any pictures of trailers on the design.
I do not want the design to be flowery in anyway as we are in the transport industry.
Simple yet effective

Business

Varno Tolt Hire Pty Ltd
Ros Penbury
Director
Ph: 03 9412 5038
Mobile: 0427 836 207
ros.penbury@varnotolt-example.com.au
www.varnotolt-example.com.au
218-224 Dunmore Road, Yarraville

```html
<!DOCTYPE html>
<html lang="en">
<head>
<meta charset="utf-8">
<title>Varno Tolt Hire Pty Ltd — Business Card</title>
<link href="https://fonts.googleapis.com/css2?family=Open+Sans:wght@400;600;700&family=PT+Sans+Narrow:wght@700&display=swap" rel="stylesheet">
<style>
  :root {
    --cherry: #ee2a33;
    --charcoal: #2b2a2c;
    --ink: #1f1f21;
    --paper: #f3f3f5;
    --backdrop: #e6e6e8;
    --white: #ffffff;
  }
  * { box-sizing: border-box; margin: 0; padding: 0; }
  html, body {
    width: 1200px; height: 800px; overflow: hidden;
    background: var(--backdrop);
    font-family: "Open Sans", Arial, sans-serif;
  }
  .stage { position: relative; width: 1200px; height: 800px; }
  .card {
    position: absolute; top: 241px;
    width: 520px; height: 318px;
    overflow: hidden;
  }

  /* Front */
  .card-front { left: 50px; background: var(--charcoal); }
  .front-brand {
    position: absolute; left: 0; right: 0; top: 104px;
    text-align: center;
    font-family: "PT Sans Narrow", "Arial Narrow", sans-serif;
    font-weight: 700; font-size: 64px; line-height: 1;
    color: var(--cherry);
  }
  .front-company {
    position: absolute; left: 0; right: 0; top: 186px;
    text-align: center;
    font-family: "PT Sans Narrow", "Arial Narrow", sans-serif;
    font-weight: 700; font-size: 26px; color: var(--white);
  }

  /* Back */
  .card-back { left: 630px; background: var(--paper); }
  .back-company {
    position: absolute; right: 22px; top: 14px;
    font-family: "PT Sans Narrow", "Arial Narrow", sans-serif;
    font-weight: 700; font-size: 22px; color: var(--ink);
  }
  .back-decor { position: absolute; inset: 0; }
  .name-block { position: absolute; left: 70px; top: 122px; }
  .person-name { font-weight: 700; font-size: 19px; color: var(--ink); line-height: 1.1; }
  .person-role {
    font-weight: 600; font-size: 11px; letter-spacing: 1.5px;
    color: var(--cherry);
  }
  .contact-list {
    position: absolute; left: 206px; top: 134px;
    list-style: none;
    font-size: 10px; line-height: 1.4; color: var(--ink);
  }
  .contact-list .strong { font-weight: 700; font-size: 12.5px; line-height: 1.3; }
  .back-brand {
    position: absolute; right: 12px; top: 218px;
    font-family: "PT Sans Narrow", "Arial Narrow", sans-serif;
    font-weight: 700; font-size: 19px; color: var(--cherry);
  }
  .back-address {
    position: absolute; left: 24px; bottom: 16px;
    font-family: "PT Sans Narrow", "Arial Narrow", sans-serif;
    font-weight: 700; font-size: 19px; color: var(--ink);
  }
</style>
</head>
<body>
<main class="stage">
  <section class="card card-front" aria-label="Card front">
    <div class="front-brand">Varno Tolt</div>
    <div class="front-company">Varno Tolt Hire Pty Ltd.</div>
  </section>

  <section class="card card-back" aria-label="Card back">
    <svg class="back-decor" width="520" height="318" viewBox="0 0 520 318" aria-hidden="true">
      <rect x="40" y="112" width="22" height="96" fill="var(--charcoal)"/>
      <rect x="32" y="106" width="34" height="96" fill="var(--cherry)"/>
      <rect x="195" y="134" width="3" height="82" fill="var(--charcoal)"/>
      <rect x="192" y="130" width="3" height="82" fill="var(--cherry)"/>
      <polygon points="520,40 520,318 350,318" fill="var(--charcoal)"/>
      <polygon points="495,50 509,50 400,220 386,220" fill="var(--cherry)"/>
      <polygon points="510,118 520,118 520,132 462,205 452,205" fill="var(--cherry)"/>
    </svg>
    <div class="back-company">Varno Tolt Hire Pty Ltd.</div>
    <div class="name-block">
      <p class="person-name">Ros Penbury</p>
      <p class="person-role">Director</p>
    </div>
    <ul class="contact-list">
      <li class="strong">tel&nbsp;&nbsp;: 03 9412 5038</li>
      <li class="strong">mob: 0427 836 207</li>
      <li>ros.penbury@varnotolt-example.com.au</li>
      <li>www.varnotolt-example.com.au</li>
    </ul>
    <div class="back-brand">Varno Tolt</div>
    <div class="back-address">218-224 Dunmore Road, Yarraville</div>
  </section>
</main>
</body>
</html>
```